valtor clinic
cards
Professional
Martin Valtor D.C. D.A.B.C.O.
Chiroptactic Orthopedist
28615 Birchmont
Detroit, MI 48235
kpm@valtorchiro.example
www.valtorchiro.example
M T W Th F S
Your Next Appointment Time

```html
<!DOCTYPE html>
<html lang="en">
<head>
<meta charset="utf-8">
<title>Valtor Clinic – Business Cards</title>
<link rel="stylesheet" href="https://fonts.googleapis.com/css2?family=Roboto:wght@400;500;700;900&display=swap">
<style>
  :root {
    --stage: #4a4a4a;
    --card: #ffffff;
    --navy: #0f2a6e;
    --blue: #1f63c6;
    --sky: #2aa8e6;
    --sky-pale: #bfe6f8;
    --green: #8cc63f;
    --ink: #222222;
    --muted: #555555;
  }
  * { margin: 0; padding: 0; box-sizing: border-box; }
  html, body { width: 1200px; height: 686px; overflow: hidden; }
  body {
    background: var(--stage);
    font-family: "Roboto", Arial, sans-serif;
    color: var(--ink);
    position: relative;
  }

  .card { position: absolute; background: var(--card); box-shadow: 0 4px 12px rgba(0,0,0,.35); }

  /* Front */
  .card-front { left: 53px; top: 144px; width: 506px; height: 365px; }
  .brand { position: absolute; left: 0; right: 0; top: 62px; text-align: center; }
  .brand-mark {
    display: inline-block; width: 26px; height: 26px; border-radius: 50%;
    background: var(--green); vertical-align: middle; margin-right: 12px;
  }
  .brand-name {
    font-weight: 900; font-size: 64px; color: var(--blue);
    letter-spacing: 1px; vertical-align: middle; text-transform: uppercase;
  }
  .brand-tag {
    display: block; font-weight: 900; font-size: 22px; color: var(--blue);
    letter-spacing: 1px; text-transform: uppercase; margin-top: -4px;
  }
  .name-band { position: absolute; left: 0; right: 0; top: 173px; height: 32px; display: flex; }
  .name-band .accent { width: 16px; background: var(--green); }
  .name-band .holder {
    width: 250px; background: var(--navy); color: #fff;
    font-weight: 700; font-style: italic; font-size: 15px;
    display: flex; align-items: center; padding-left: 14px;
  }
  .name-band .title {
    flex: 1; background: linear-gradient(90deg, var(--sky-pale), var(--sky));
    color: var(--navy); font-size: 15px;
    display: flex; align-items: center; padding-left: 12px;
  }
  .contacts { position: absolute; left: 0; right: 0; top: 224px; font-size: 13px; color: var(--muted); }
  .contacts .row { display: flex; justify-content: center; gap: 22px; margin-bottom: 10px; }
  .contacts .item { display: flex; align-items: center; gap: 6px; }
  .contacts svg { width: 14px; height: 14px; fill: var(--blue); }

  /* Back */
  .card-back { left: 619px; top: 350px; width: 528px; height: 329px; }
  .appt-title { position: absolute; left: 26px; top: 30px; font-size: 18px; font-weight: 500; text-transform: uppercase; }
  .appt-mark { position: absolute; right: 30px; top: 26px; width: 18px; height: 18px; border-radius: 50%; background: var(--green); }
  .field { position: absolute; left: 26px; right: 26px; font-size: 15px; display: flex; align-items: baseline; }
  .field .dots { flex: 1; border-bottom: 2px dotted #777; margin: 0 4px; height: 1px; }
  .field .short { flex: 0 0 200px; }
  .days { position: absolute; left: 26px; right: 26px; top: 176px; display: flex; justify-content: space-between; font-size: 15px; }
  .day { display: flex; align-items: center; gap: 7px; }
  .day .box { width: 20px; height: 20px; border: 1.5px solid #555; }
  .notice { position: absolute; left: 26px; top: 218px; font-size: 14px; }
  .back-band { position: absolute; left: 26px; right: 26px; top: 250px; height: 22px; display: flex; }
  .back-band .accent { width: 14px; background: var(--green); }
  .back-band .bar {
    flex: 1; background: linear-gradient(90deg, var(--navy), var(--blue) 60%, var(--sky));
    color: #fff; font-size: 11px; display: flex; align-items: center; justify-content: flex-end; padding-right: 130px;
  }
</style>
</head>
<body>

<section class="card card-front">
  <div class="brand">
    <span class="brand-mark"></span><span class="brand-name">Valtor</span>
    <span class="brand-tag">Chiropractic Clinic</span>
  </div>

  <div class="name-band">
    <div class="accent"></div>
    <div class="holder">Martin Valtor D.C. D.A.B.C.O.</div>
    <div class="title">Chiroptactic Orthopedist</div>
  </div>

  <div class="contacts">
    <div class="row">
      <span class="item">
        <svg viewBox="0 0 24 24"><path d="M6.6 10.8a15 15 0 0 0 6.6 6.6l2.2-2.2c.3-.3.7-.4 1-.2 1.1.4 2.3.6 3.6.6.6 0 1 .4 1 1V20c0 .6-.4 1-1 1A17 17 0 0 1 3 4c0-.6.4-1 1-1h3.5c.6 0 1 .4 1 1 0 1.3.2 2.5.6 3.6.1.3 0 .7-.2 1z"/></svg>
        313 555 0142
      </span>
      <span class="item">
        <svg viewBox="0 0 24 24"><path d="M5 3h14v5H5zM3 9h18v8h-3v4H6v-4H3zm5 6v4h8v-4z"/></svg>
        313 555 0178
      </span>
    </div>
    <div class="row">
      <span class="item">
        <svg viewBox="0 0 24 24"><path d="M2 5h20v14H2zm2 2v.5l8 5 8-5V7z"/></svg>
        kpm@valtorchiro.example
      </span>
      <span class="item">
        <svg viewBox="0 0 24 24"><circle cx="12" cy="12" r="10"/></svg>
        www.valtorchiro.example
      </span>
    </div>
    <div class="row">
      <span class="item">28615 Birchmont, Detroit, MI 48235</span>
    </div>
  </div>
</section>

<section class="card card-back">
  <h2 class="appt-title">Your Appointment</h2>
  <span class="appt-mark"></span>

  <div class="field" style="top:66px">Name :<span class="dots"></span></div>
  <div class="field" style="top:100px">Date:<span class="dots"></span>Time:<span class="dots short"></span>am/pm</div>
  <div class="field" style="top:134px">Next Appointment Time:<span class="dots short" style="flex:0 0 180px"></span></div>

  <div class="days">
    <span class="day"><span class="box"></span>Mon</span>
    <span class="day"><span class="box"></span>Tue</span>
    <span class="day"><span class="box"></span>Wed</span>
    <span class="day"><span class="box"></span>Thu</span>
    <span class="day"><span class="box"></span>Fri</span>
    <span class="day"><span class="box"></span>Sat</span>
  </div>

  <p class="notice">We appreciate a 24 hr. notice for cancellations</p>

  <div class="back-band">
    <div class="accent"></div>
    <div class="bar">www.valtorchiro.example</div>
  </div>
</section>

</body>
</html>
```